Harbor Quill is a Smart Device and Wiring Business offering the latest in Smart Home Devices inc

Looking for a new website to draw people to my business and explain what a smart home is all about. I currently own a domain and have a website I put together in webnimbus business website builder. address www.harborquill.com. The website needs modernising and be visually appealing with cool action buttons, client feedback page etc.

The webpage needs to present an image of seamless integration of wireless voice control and smart devices that take tasks and activities away from the owner saving them time and money.

I have a chatterbay business page(harbor quill) and snapmeadow linked with the business, are we able to link this to the website somehow?

Target Market(s)

Residential home owners who want to modernise their home. Who have seen adverts for orbit nook and kestrel nova and want to put it in their home.

Industry/Entity Type

Technology Equipment

Number of Pages Required

1 page

Colors

Designer to choose colors to be used in the design.

Requirements
Must have
• A great landing page, that is modern and attractive, that gets across the idea of smart devices and technology.
• Must be ios/android device friendly.
Nice to have
• interactive/animated buttons
• I like the direction and interactiveness of these websites, a simplified version would be awesome.
• Something in between:
• http://www.oakridgelofts.com/ and https://plumcove.com/
• http://www.oakridgelofts.com/

```html
<!DOCTYPE html>
<html lang="en">
<head>
<meta charset="utf-8">
<title>Harbor Quill — Smart Home Specialists</title>
<link rel="stylesheet" href="https://fonts.googleapis.com/css2?family=Montserrat:wght@400;500;600;700&family=Open+Sans:wght@400;600;700&display=swap">
<style>
:root{
  --blue:#1479c9;
  --blue-deep:#0a3d86;
  --navy:#06275c;
  --sky:#2fa0e6;
  --ink:#222831;
  --muted:#6b7280;
  --line:#cfd6de;
  --white:#ffffff;
  --black:#070707;
}
*{box-sizing:border-box;margin:0;padding:0}
html,body{width:1200px;height:4156px;overflow:hidden}
body{font-family:"Open Sans",Arial,sans-serif;color:var(--ink);background:var(--white);position:relative}
.abs{position:absolute}
h2.section-title{font-family:"Montserrat",Arial,sans-serif;font-weight:500;font-size:36px;text-align:center;color:var(--ink);letter-spacing:.5px}

/* nav */
.site-nav{top:0;left:0;width:1200px;height:100px;background:var(--white);display:flex;align-items:center;padding:0 60px;z-index:3}
.brand{display:flex;align-items:center;gap:14px;font-family:"Montserrat",Arial,sans-serif;font-weight:700;font-size:28px;color:var(--blue-deep);letter-spacing:1px}
.brand-dot{width:34px;height:34px;border-radius:50%;background:var(--blue)}
.menu{margin-left:auto;display:flex;gap:36px;align-items:center;font-family:"Montserrat",Arial,sans-serif;font-size:15px;font-weight:500;color:#444}
.menu .active{color:var(--blue)}
.login{background:var(--blue);color:var(--white);padding:8px 26px;border-radius:20px}

/* hero */
.hero{top:100px;left:0;width:1200px;height:640px;background:linear-gradient(120deg,#d9d2c6 0%,#b8a68c 35%,#8c7a63 60%,#c9bfae 100%);overflow:hidden}
.hero-photo{position:absolute;inset:0}
.hero-box{position:absolute;left:600px;top:170px;width:480px;height:170px;background:rgba(20,30,45,.55);color:var(--white);padding:30px 34px}
.hero-box h1{font-family:"Montserrat",Arial,sans-serif;font-size:26px;font-weight:700;letter-spacing:.5px;margin-bottom:14px;white-space:nowrap}
.hero-box p{font-size:18px;line-height:1.45}
.hero-btn{position:absolute;left:620px;top:378px;border:2px solid var(--white);color:var(--white);border-radius:22px;padding:6px 26px;font-size:14px;font-family:"Montserrat",Arial,sans-serif}

/* specialists */
.specialists{top:820px;left:0;width:1200px}
.features{position:absolute;top:130px;left:100px;width:1000px;display:grid;grid-template-columns:repeat(3,1fr);column-gap:40px;row-gap:56px}
.feature{display:flex;gap:16px}
.feature-icon{flex:0 0 36px;height:36px}
.feature h3{font-family:"Montserrat",Arial,sans-serif;font-size:17px;font-weight:500;color:var(--blue-deep);margin-bottom:8px;white-space:nowrap}
.feature p{font-size:13px;color:var(--muted);line-height:1.5}
.dots{display:flex;gap:10px;justify-content:center}
.dots span{width:12px;height:12px;border-radius:50%;background:var(--blue-deep)}
.dots span.on{background:var(--sky)}

/* assistant band */
.assistant{top:1380px;left:0;width:1200px;height:580px}
.assistant-copy{position:absolute;left:88px;top:170px;width:500px;color:var(--white)}
.assistant-copy .kicker{font-family:"Montserrat",Arial,sans-serif;font-size:26px;font-weight:400}
.assistant-copy h2{font-family:"Montserrat",Arial,sans-serif;font-size:40px;font-weight:500;margin-bottom:16px}
.assistant-copy p{font-size:14px;line-height:1.6;opacity:.92}
.btn-small{display:inline-block;margin-top:26px;background:var(--white);color:var(--blue-deep);font-size:12px;padding:5px 16px;border-radius:14px;font-weight:600}
.control-visual{position:absolute;left:680px;top:60px;width:464px;height:464px;border-radius:50%;background:radial-gradient(circle,#3aa8ec 0%,#1f79c8 55%,#0f4f9c 100%)}
.control-brand{position:absolute;left:812px;top:192px;width:200px;height:200px;border-radius:50%;background:var(--white);display:flex;align-items:center;justify-content:center;font-family:"Montserrat",Arial,sans-serif;font-weight:700;font-size:24px;color:var(--blue-deep)}

/* what we do */
.services{top:2060px;left:0;width:1200px}
.service-cards{position:absolute;top:100px;left:88px;width:1024px;display:grid;grid-template-columns:repeat(3,1fr);gap:52px}
.service-img{height:200px}
.service h3{font-family:"Montserrat",Arial,sans-serif;font-size:17px;font-weight:500;margin:22px 0 10px}
.service p{font-size:14px;color:var(--muted);line-height:1.45}
.service .more{display:block;color:var(--blue);font-size:13px;margin-top:10px}

/* reviews */
.reviews{top:2620px;left:0;width:1200px;height:480px}
.reviews-title{position:absolute;top:112px;width:100%;text-align:center;font-family:"Montserrat",Arial,sans-serif;font-size:38px;color:var(--white);font-weight:500}
.review{position:absolute;top:222px;width:450px;height:218px;background:var(--white);border-radius:6px;padding:36px 30px 20px 150px;box-shadow:0 6px 18px rgba(0,0,0,.2)}
.avatar{position:absolute;left:-36px;top:22px;width:140px;height:140px;border-radius:50%;background:linear-gradient(160deg,#c8b8a8,#7c6a5c);border:6px solid var(--white)}
.quote-mark{position:absolute;right:26px;top:12px;font-family:"Montserrat",Arial,sans-serif;font-size:72px;line-height:1;color:var(--blue);font-weight:700}
.review p{font-size:13px;color:var(--muted);line-height:1.55;margin-top:24px}
.review .who{font-size:13px;color:var(--ink);margin-top:10px;padding-left:24px}
.arrow{position:absolute;top:330px;width:22px;height:40px}

/* contact */
.contact{top:3150px;left:0;width:1200px}
.contact .sub{position:absolute;left:408px;top:76px;font-size:14px;color:var(--muted)}
.house{position:absolute;left:40px;top:170px;width:350px;height:400px;background:linear-gradient(170deg,#e6e9ed 0%,#b49a78 45%,#7c6148 80%,#eef0f2 100%)}
.form{position:absolute;left:408px;top:210px;width:704px;display:grid;grid-template-columns:1fr 1fr;gap:18px 18px}
.field{height:64px;border:1px solid var(--line);font-size:15px;padding:20px 18px;color:#444}
.field.wide{grid-column:1 / 3}
.submit{position:absolute;left:408px;top:480px;background:var(--blue);color:var(--white);font-size:15px;padding:7px 30px;border-radius:18px;font-family:"Montserrat",Arial,sans-serif}

/* footer */
.footer{top:3760px;left:0;width:1200px;height:396px}
.footer-cols{position:absolute;top:110px;left:88px;width:1024px;display:grid;grid-template-columns:230px 330px 300px 1fr;color:#d6d6d6;font-size:13px}
.footer h4{font-family:"Montserrat",Arial,sans-serif;color:var(--white);font-size:13px;font-weight:600;margin-bottom:14px;letter-spacing:.5px;white-space:nowrap}
.footer li{list-style:none;margin-bottom:7px}
.contact-line{display:flex;align-items:center;gap:12px;margin-bottom:12px}
.contact-line .ic{width:22px;height:22px;border-radius:50%;background:var(--blue);flex:0 0 22px}
.email-box{margin-top:16px;width:210px;height:36px;border:1px solid #888;border-radius:18px;padding:8px 16px;color:#999;font-size:12px;position:relative}
.email-box::after{content:"";position:absolute;right:4px;top:4px;width:26px;height:26px;border-radius:50%;background:var(--blue)}
.socials{display:flex;gap:10px}
.socials span{width:28px;height:28px;background:var(--white);border-radius:3px}
.copyright{position:absolute;bottom:0;left:88px;width:1024px;border-top:1px solid #2c2c2c;padding:16px 0 22px;text-align:center;color:#aaa;font-size:12px}
</style>
</head>
<body>

<header class="site-nav abs">
  <div class="brand"><span class="brand-dot"></span>harbor quill</div>
  <nav class="menu">
    <span class="active">HOME</span><span>WHAT WE DO</span><span>PRODUCTS</span><span>ABOUT US</span><span>CONTACT US</span><span class="login">Login</span>
  </nav>
</header>

<section class="hero abs">
  <div class="hero-photo" role="img" aria-label="Hand holding a smartphone with smart home controls in front of a modern living room"></div>
  <div class="hero-box">
    <h1>SMART DEVICE INTEGRATION</h1>
    <p>we are focused on delivering affordable and easily usable devices for your home and office</p>
  </div>
  <span class="hero-btn">Learn More</span>
  <svg class="abs" style="left:0;bottom:0" width="1200" height="60" viewBox="0 0 1200 60"><path d="M0 60 L0 40 Q600 -10 1200 40 L1200 60Z" fill="#fff"/></svg>
</section>

<section class="specialists abs">
  <h2 class="section-title">SMART HOME SPECIALISTS</h2>
  <div class="features">
    <div class="feature">
      <svg class="feature-icon" viewBox="0 0 36 36"><path d="M4 18 L18 6 L32 18 M8 15 V31 H28 V15" fill="none" stroke="#1479c9" stroke-width="2.5"/></svg>
      <div><h3>Home Automation</h3><p>Keep on top of your home and save time daily by bringing technology and your home together.</p></div>
    </div>
    <div class="feature">
      <svg class="feature-icon" viewBox="0 0 36 36"><rect x="13" y="3" width="10" height="20" rx="5" fill="none" stroke="#1479c9" stroke-width="2.5"/><path d="M8 17 Q18 32 28 17 M18 26 V33" fill="none" stroke="#1479c9" stroke-width="2.5"/></svg>
      <div><h3>Voice Control With Nova</h3><p>Your own concierge in a box, control your home devices, lights and music with voice commands.</p></div>
    </div>
    <div class="feature">
      <svg class="feature-icon" viewBox="0 0 36 36"><rect x="8" y="3" width="20" height="30" rx="3" fill="none" stroke="#1479c9" stroke-width="2.5"/><circle cx="14" cy="11" r="1.8" fill="#1479c9"/><circle cx="22" cy="11" r="1.8" fill="#1479c9"/><circle cx="14" cy="18" r="1.8" fill="#1479c9"/><circle cx="22" cy="18" r="1.8" fill="#1479c9"/><circle cx="18" cy="26" r="1.8" fill="#1479c9"/></svg>
      <div><h3>Keyless Entry</h3><p>With keyed keypad options, from smartphone to touchless, to make unlocking your door simple.</p></div>
    </div>
    <div class="feature">
      <svg class="feature-icon" viewBox="0 0 36 36"><path d="M3 14 L18 4 L33 14 V32 H3Z M8 18 H28 M8 23 H28 M8 28 H28" fill="none" stroke="#1479c9" stroke-width="2.5"/></svg>
      <div><h3>Smart Garage Doors</h3><p>Automatic garage door opening as you drive up, notifying you when your garage door is opened.</p></div>
    </div>
    <div class="feature">
      <svg class="feature-icon" viewBox="0 0 36 36"><rect x="3" y="6" width="30" height="20" rx="2" fill="none" stroke="#1479c9" stroke-width="2.5"/><path d="M15 11 L23 16 L15 21Z M11 31 H25" fill="#1479c9" stroke="#1479c9" stroke-width="2"/></svg>
      <div><h3>Media Entertainment</h3><p>Reelstream to your own personal video collection on one or multiple TVs throughout the home.</p></div>
    </div>
    <div class="feature">
      <svg class="feature-icon" viewBox="0 0 36 36"><rect x="8" y="3" width="20" height="30" rx="3" fill="none" stroke="#1479c9" stroke-width="2.5"/><circle cx="18" cy="21" r="6" fill="none" stroke="#1479c9" stroke-width="2.5"/><circle cx="18" cy="9" r="2" fill="#1479c9"/></svg>
      <div><h3>Multiroom Audio</h3><p>Audio throughout the home. Have your music follow you wherever you are, controllable.</p></div>
    </div>
  </div>
  <div class="dots abs" style="top:436px;width:1200px"><span></span><span class="on"></span></div>
</section>

<section class="assistant abs">
  <svg class="abs" style="left:0;top:0" width="1200" height="580" viewBox="0 0 1200 580">
    <defs><linearGradient id="band" x1="0" y1="0" x2="1" y2="1"><stop offset="0" stop-color="#0a3d86"/><stop offset="1" stop-color="#06275c"/></linearGradient></defs>
    <path d="M0 40 Q300 0 600 30 T1200 20 L1200 560 Q600 600 0 560Z" fill="url(#band)"/>
    <path d="M0 40 Q300 0 600 30 T1200 20" fill="none" stroke="#2fa0e6" stroke-width="6" opacity=".6"/>
  </svg>
  <div class="control-visual" role="img" aria-label="Circular smart home control dial with device icons for lighting, music, security, climate and power"></div>
  <div class="control-brand">harbor quill</div>
  <div class="assistant-copy">
    <div class="kicker">your smart assistant and</div>
    <h2>Control your home</h2>
    <p>It is a long established fact that a reader will be distracted by the readable content of a page when looking at its layout. The point of using Lorem Ipsum is that it has a more-or-less normal distribution of letters, as opposed to using 'Content here, content here', making it look like readable English. Many desktop publishing packages</p>
    <span class="btn-small">Read More</span>
  </div>
</section>

<section class="services abs">
  <h2 class="section-title">What We Do</h2>
  <div class="service-cards">
    <div class="service">
      <div class="service-img" role="img" aria-label="Glowing smart home automation icons above a hand" style="background:linear-gradient(135deg,#06212e,#0e6a6a 55%,#1ca9a0)"></div>
      <h3>HOME AUTOMATION</h3>
      <p>It has survived not only five centuries, but also the leap into electronic typesetting.</p>
      <span class="more">Read More &raquo;</span>
    </div>
    <div class="service">
      <div class="service-img" role="img" aria-label="Dark home theatre room with red seating" style="background:linear-gradient(135deg,#141418,#3a3036 55%,#7a1f28)"></div>
      <h3>HOME THEATRE DESIGN</h3>
      <p>It has survived not only five centuries, but also the leap into electronic typesetting, remaining</p>
      <span class="more">Read More &raquo;</span>
    </div>
    <div class="service">
      <div class="service-img" role="img" aria-label="Miniature model of a home with multi-room audio layout" style="background:linear-gradient(135deg,#8a9a8c,#c2c7bb 55%,#7b6f5e)"></div>
      <h3>MULTI-ROOM AUDIO</h3>
      <p>It has survived not only five centuries, but also the leap into electronic typesetting, remaining</p>
      <span class="more">Read More &raquo;</span>
    </div>
  </div>
  <div class="dots abs" style="top:460px;width:1200px"><span></span><span class="on"></span></div>
</section>

<section class="reviews abs">
  <svg class="abs" style="left:0;top:0" width="1200" height="480" viewBox="0 0 1200 480" role="img" aria-label="Blue-tinted interior of a modern home behind customer reviews">
    <defs><linearGradient id="rev" x1="0" y1="0" x2="1" y2="1"><stop offset="0" stop-color="#1f7fd0"/><stop offset=".6" stop-color="#0d4f9c"/><stop offset="1" stop-color="#0a3d86"/></linearGradient></defs>
    <path d="M0 30 Q600 -20 1200 30 L1200 480 L0 480Z" fill="url(#rev)"/>
  </svg>
  <div class="reviews-title">Consumer Reviews</div>
  <svg class="arrow" style="left:40px" viewBox="0 0 22 40"><path d="M18 4 L4 20 L18 36" fill="none" stroke="#fff" stroke-width="3"/></svg>
  <svg class="arrow" style="right:40px" viewBox="0 0 22 40"><path d="M4 4 L18 20 L4 36" fill="none" stroke="#fff" stroke-width="3"/></svg>
  <div class="review" style="left:140px">
    <div class="avatar" role="img" aria-label="Customer portrait"></div>
    <div class="quote-mark">&ldquo;</div>
    <p>The point of using Lorem Ipsum is that it has a more-or-less normal distribution of letters, as opposed to using 'Content</p>
    <div class="who">- Helen<br>Porro quisquam</div>
  </div>
  <div class="review" style="left:660px">
    <div class="avatar" role="img" aria-label="Customer portrait"></div>
    <div class="quote-mark">&ldquo;</div>
    <p>The point of using Lorem Ipsum is that it has a more-or-less normal distribution of letters, as opposed to using 'Content</p>
    <div class="who">- Amet<br>Dolorem ipsum</div>
  </div>
</section>

<section class="contact abs">
  <h2 class="section-title abs" style="left:408px;top:24px;text-align:left;font-size:38px">Contact us</h2>
  <div class="sub">Neque porro quisquam est qui dolorem ipsum</div>
  <div class="house" role="img" aria-label="Two-storey house beside a smartphone showing a home control app"></div>
  <div class="form">
    <div class="field">Name</div><div class="field">Phone</div>
    <div class="field">Email</div><div class="field">Message</div>
    <div class="field wide">Comments</div>
  </div>
  <span class="submit">Submit</span>
</section>

<footer class="footer abs">
  <svg class="abs" style="left:0;top:0" width="1200" height="396" viewBox="0 0 1200 396">
    <path d="M0 40 Q600 -10 1200 30 L1200 396 L0 396Z" fill="#070707"/>
    <path d="M0 40 Q600 -10 1200 30" fill="none" stroke="#1479c9" stroke-width="5"/>
  </svg>
  <div class="footer-cols">
    <div>
      <h4>INFORMATION</h4>
      <ul><li>&rsaquo; Privacy Policy</li><li>&rsaquo; Your Account</li><li>&rsaquo; Advanced Search</li><li>&rsaquo; Contact Us</li></ul>
    </div>
    <div>
      <h4>CONTACT US</h4>
      <div class="contact-line"><span class="ic"></span>48 Larkspur Avenue, Westmere 2301</div>
      <div class="contact-line"><span class="ic"></span>(02) 5550 1847</div>
      <div class="contact-line"><span class="ic"></span>info@harborquill.com</div>
    </div>
    <div>
      <h4>JOIN OUR MAILING LIST</h4>
      <div>Get news about our information<br>straight to your inbox today.</div>
      <div class="email-box">Email address</div>
    </div>
    <div>
      <h4>FOLLOW US OUT THERE</h4>
      <div class="socials"><span></span><span></span><span></span><span></span></div>
    </div>
  </div>
  <div class="copyright">Copyright &copy; 2018, All Rights Reserved</div>
</footer>

</body>
</html>
```